Business Card Design

WE are looking for a premium quality Business Cards for a Law Firm . Copies of our current business card is attached.
Updates

Went on vacation/holiday

Contact Information for Business Card

xyz

```html
<!DOCTYPE html>
<html lang="en">
<head>
<meta charset="utf-8">
<title>Harrowgate Lawyers – Business Card</title>
<link href="https://fonts.googleapis.com/css2?family=Tinos:wght@400;700&display=swap" rel="stylesheet">
<style>
  :root {
    --backdrop: #1d1d20;
    --card-green: #0f2a1e;
    --card-green-deep: #0b2117;
    --gold: #c9a45c;
    --ivory: #f4f1ea;
  }
  * { box-sizing: border-box; margin: 0; padding: 0; }
  html, body {
    width: 1200px; height: 780px; overflow: hidden;
    background: var(--backdrop);
    font-family: "Tinos", "Times New Roman", serif;
  }
  .canvas { position: relative; width: 1200px; height: 780px; }
  .card {
    position: absolute; top: 222px;
    width: 550px; height: 336px;
    background: var(--card-green);
    border-bottom: 3px solid var(--gold);
    border-left: 2px solid var(--gold);
    overflow: hidden;
  }
  .card--front { left: 33px; }
  .card--back { left: 617px; }

  /* Front: centred name block */
  .brand {
    position: absolute; inset: 0;
    display: flex; flex-direction: column; align-items: center; justify-content: center;
    gap: 14px;
  }
  .brand__ring {
    width: 74px; height: 74px; border-radius: 50%;
    border: 5px solid var(--gold);
  }
  .brand__name {
    color: var(--ivory); font-weight: 700; text-align: center; line-height: 1;
  }
  .brand__name .firm { display: block; font-size: 44px; letter-spacing: 1px; }
  .brand__name .kind { display: block; font-size: 15px; letter-spacing: 11px; margin-top: 8px; padding-left: 11px; }
  .brand__rule { display: flex; align-items: center; gap: 10px; width: 330px; }
  .brand__rule span { flex: 1; height: 1.5px; background: var(--gold); }

  /* Back */
  .tab {
    position: absolute; top: 0; right: 40px;
    width: 16px; height: 58px; background: var(--gold);
  }
  .person {
    position: absolute; top: 20px; right: 66px; text-align: right;
  }
  .person__name { color: var(--gold); font-weight: 700; font-size: 28px; letter-spacing: 1px; line-height: 1.1; }
  .person__role { color: var(--ivory); font-weight: 700; font-size: 13px; line-height: 1.35; }
  .seal {
    position: absolute; right: 18px; top: 112px;
    width: 190px; height: 190px; border-radius: 50%;
    background: radial-gradient(circle at 40% 35%, #173a2a, var(--card-green-deep));
    border: 8px solid #0a1c13;
    box-shadow: inset 0 3px 6px rgba(255,255,255,0.18), 0 6px 14px rgba(0,0,0,0.5);
  }
  .mini-brand {
    position: absolute; left: 34px; top: 100px;
    display: flex; align-items: center; gap: 12px;
  }
  .mini-brand__ring { width: 42px; height: 42px; border-radius: 50%; border: 3px solid var(--gold); }
  .mini-brand__name { color: var(--ivory); font-weight: 700; line-height: 1; }
  .mini-brand__name .firm { display: block; font-size: 24px; }
  .mini-brand__name .kind { display: block; font-size: 9px; letter-spacing: 6px; margin-top: 4px; }
  .address {
    position: absolute; left: 34px; top: 156px;
    color: var(--ivory); font-weight: 700; font-size: 14px; line-height: 1.35;
  }
  .contacts {
    position: absolute; left: 34px; top: 226px; list-style: none;
    color: var(--ivory); font-weight: 700; font-size: 14px; line-height: 1.35;
  }
  .contacts li { display: flex; align-items: center; gap: 8px; margin-bottom: 2px; }
  .contacts svg { width: 13px; height: 13px; flex: none; }
</style>
</head>
<body>
<main class="canvas">

  <section class="card card--front" aria-label="Card front">
    <div class="brand">
      <div class="brand__ring"></div>
      <div class="brand__name">
        <span class="firm">HARROWGATE</span>
        <span class="kind">LAWYERS</span>
      </div>
      <div class="brand__rule"><span></span><span></span></div>
    </div>
  </section>

  <section class="card card--back" aria-label="Card back">
    <div class="tab"></div>
    <div class="person">
      <p class="person__name">DANIEL MARSH</p>
      <p class="person__role">Director and Principal Solicitor</p>
      <p class="person__role">MBA, Juris Doctor</p>
    </div>
    <div class="seal"></div>

    <div class="mini-brand">
      <div class="mini-brand__ring"></div>
      <div class="mini-brand__name">
        <span class="firm">HARROWGATE</span>
        <span class="kind">LAWYERS</span>
      </div>
    </div>

    <p class="address">Level 3, Ellery House,<br>210 Ellery Terrace,<br>Kelvin Park, QLD 4100</p>

    <ul class="contacts">
      <li>
        <svg viewBox="0 0 24 24" fill="none" stroke="var(--gold)" stroke-width="2.4" stroke-linecap="round"><path d="M5 3h4l2 5-2.5 1.5a11 11 0 0 0 6 6L16 13l5 2v4a2 2 0 0 1-2 2A17 17 0 0 1 3 5a2 2 0 0 1 2-2z"/></svg>
        +61 7 3000 1425
      </li>
      <li>
        <svg viewBox="0 0 24 24" fill="none" stroke="var(--gold)" stroke-width="2.4"><rect x="6" y="2" width="12" height="20" rx="2"/><line x1="11" y1="18" x2="13" y2="18"/></svg>
        +61 0400 000 417
      </li>
      <li>
        <svg viewBox="0 0 24 24" fill="none" stroke="var(--gold)" stroke-width="2.2"><circle cx="12" cy="12" r="10"/><ellipse cx="12" cy="12" rx="4" ry="10"/><line x1="2" y1="12" x2="22" y2="12"/></svg>
        www.harrowgatelawyers.com.au
      </li>
      <li>
        <svg viewBox="0 0 24 24" fill="none" stroke="var(--gold)" stroke-width="2.2"><rect x="2" y="5" width="20" height="14" rx="1"/><path d="M2 6l10 7 10-7"/></svg>
        daniel@harrowgatelawyers.com.au
      </li>
    </ul>
  </section>

</main>
</body>
</html>
```